Gentleman's grooming products require a business card

I need a business card that incorporates the logo [ or parts of ] that we had Pixel Hive design for us as uploaded.

We sell online, mens grooming products including moustache waxes, beard oils and shaving accessories.
We want a card that is classy, professional and a card that shouts mens products.

Target Market(s)

Young professional male market

Industry/Entity Type

Business

Contact Information for Business Card

Ross and Edith Carwell
Lather and Lore
Purveyors of gentleman's stiffeners and grooming requisites
M :0418529647
E : ross@latherandlore.com.au
E : edith@latherandlore.com.au
E : sales@theblokesbalmery.com.au

W : www.latherandlore.com.au

Requirements
Must have
• Class
Nice to have
• Professionalism

```html
<!DOCTYPE html>
<html lang="en">
<head>
<meta charset="utf-8">
<title>Lather &amp; Lore — Business Card</title>
<link rel="stylesheet" href="https://fonts.googleapis.com/css2?family=Pinyon+Script&family=Marcellus&family=Roboto+Condensed:wght@300;400;500&display=swap">
<style>
  :root {
    --page: #ffffff;
    --card: #eceeee;
    --card-shade: #e2e5e5;
    --ink: #2a1a12;
    --cyan: #00ffff;
    --white: #ffffff;
  }
  html, body {
    margin: 0;
    padding: 0;
    width: 1200px;
    height: 784px;
    overflow: hidden;
    background: var(--page);
  }
  .card {
    position: absolute;
    left: 132px;
    top: 133px;
    width: 935px;
    height: 523px;
    background: linear-gradient(180deg, var(--card) 0%, var(--card-shade) 100%);
    color: var(--ink);
  }
  .brand-dot {
    position: absolute;
    left: 92px;
    top: 118px;
    width: 62px;
    height: 62px;
    border-radius: 50%;
    background: var(--ink);
  }
  .owners {
    position: absolute;
    left: 229px;
    top: 52px;
    margin: 0;
    font-family: "Pinyon Script", cursive;
    font-size: 50px;
    font-weight: 400;
    line-height: 1;
    white-space: nowrap;
  }
  .brand-name {
    position: absolute;
    left: 224px;
    top: 126px;
    margin: 0;
    font-family: "Marcellus", serif;
    font-size: 98px;
    font-weight: 400;
    line-height: 1;
    white-space: nowrap;
  }
  .tagline {
    position: absolute;
    left: 224px;
    top: 229px;
    margin: 0;
    font-family: "Roboto Condensed", sans-serif;
    font-weight: 300;
    font-size: 30px;
    line-height: 1;
    white-space: nowrap;
    letter-spacing: -0.2px;
  }
  .contacts {
    position: absolute;
    left: 478px;
    top: 291px;
    margin: 0;
    padding: 0;
    list-style: none;
    font-family: "Roboto Condensed", sans-serif;
    font-weight: 500;
    font-size: 21px;
    line-height: 29px;
    color: #111;
  }
  .contacts li { white-space: nowrap; }
  .contacts .label {
    display: inline-block;
    width: 18px;
  }
  .contacts .sep {
    display: inline-block;
    width: 20px;
  }
  .rule-dark {
    position: absolute;
    left: 0;
    top: 420px;
    width: 167px;
    height: 9px;
    background: var(--ink);
  }
  .rule-cyan {
    position: absolute;
    left: 175px;
    top: 420px;
    width: 760px;
    height: 9px;
    background: var(--cyan);
  }
  .block-cyan {
    position: absolute;
    left: 0;
    top: 436px;
    width: 167px;
    height: 87px;
    background: var(--cyan);
  }
  .footer-band {
    position: absolute;
    left: 175px;
    top: 436px;
    width: 760px;
    height: 87px;
    background: var(--ink);
  }
  .website {
    position: absolute;
    left: 303px;
    top: 18px;
    margin: 0;
    font-family: "Roboto Condensed", sans-serif;
    font-weight: 400;
    font-size: 31px;
    line-height: 1;
    color: var(--white);
    white-space: nowrap;
  }
</style>
</head>
<body>
  <div class="card">
    <span class="brand-dot" aria-hidden="true"></span>
    <p class="owners">Ross &amp; Edith Carwell</p>
    <h1 class="brand-name">Lather &amp; Lore</h1>
    <p class="tagline">Purveyors of gentleman's stiffeners and grooming requisites</p>
    <ul class="contacts">
      <li><span class="label">M</span><span class="sep">:</span>0418529647</li>
      <li><span class="label">E</span><span class="sep">:</span>ross@latherandlore.com.au</li>
      <li><span class="label">E</span><span class="sep">:</span>edith@latherandlore.com.au</li>
      <li><span class="label">E</span><span class="sep">:</span>sales@theblokesbalmery.com.au</li>
    </ul>
    <span class="rule-dark"></span>
    <span class="rule-cyan"></span>
    <span class="block-cyan"></span>
    <div class="footer-band">
      <p class="website">www.latherandlore.com.au</p>
    </div>
  </div>
</body>
</html>
```